Harrowgate Distillery Bottle Label Design

We need a label design for a product called "Cedar Lorne Straight Bourbon Whiskey". The bottle has two embossments on the side and an image printed on the back that will show through when looking from the front (shown in the attached image). It's made of 30% rye and 70% corn; images of the ingredients can be incorporated into the label design. We are a distillery that produces whiskey and bourbon from local farmers around the area. We focus on the quality of the ingredients and using the recipes passed down from generation to generation. We like a straight forward design using two colors maximum. The background will be brown once filled with the bourbon, so it must contrast against it (i.e. white and other lighter colors). The Harrowgate Distillery logo must be present on the bottle front, as well as 750 ml, 84 PROOF, 42% ALC/VOL.

Target Market(s)

Craft whiskey consumers.

Industry/Entity Type

Product

Colors
fee18a
fbe7d2
fff3d1
fefcee
fefdec
fdf9cf

Requirements
Must have
• 750 ml, 84 PROOF, 42% ALC/VOL. Aged for 3 years.The Harrowgate Distillery logo must be present on the bottle. Only two colors on label.
Nice to have
• Story of how we are a micro distillery making hand crafted whiskey.
Should not have
• False or misleading print.

```html
<!DOCTYPE html>
<html lang="en">
<head>
<meta charset="utf-8">
<title>Harrowgate Distillery – Cedar Lorne Straight Bourbon Whiskey Label</title>
<link rel="stylesheet" href="https://fonts.googleapis.com/css2?family=Open+Sans:wdth,wght@75..100,400..800&display=swap">
<style>
  :root {
    --bourbon: #c85a1c;
    --bourbon-deep: #a8441a;
    --label-ink: #fefcee;
  }
  html, body {
    margin: 0;
    padding: 0;
    width: 1200px;
    height: 1000px;
    overflow: hidden;
    background: var(--bourbon);
  }
  .canvas {
    width: 1200px;
    height: 1000px;
    display: flex;
    align-items: center;
    justify-content: center;
    background: radial-gradient(ellipse at 50% 45%, var(--bourbon) 0%, var(--bourbon) 55%, var(--bourbon-deep) 100%);
  }
  .label {
    width: 780px;
    display: flex;
    flex-direction: column;
    align-items: center;
    color: var(--label-ink);
    font-family: "Open Sans", Arial, sans-serif;
    text-align: center;
  }
  .brand {
    display: flex;
    flex-direction: column;
    align-items: center;
  }
  .brand-dot {
    width: 70px;
    height: 70px;
    border-radius: 50%;
    background: var(--label-ink);
    margin-bottom: 22px;
  }
  .brand-name {
    font-weight: 700;
    font-stretch: 90%;
    line-height: 1;
  }
  .brand-name .line-main {
    display: block;
    font-size: 64px;
    letter-spacing: -0.5px;
  }
  .brand-name .line-sub {
    display: block;
    font-size: 30px;
    letter-spacing: 5px;
    margin-top: 6px;
    padding-top: 6px;
    border-top: 2px solid var(--label-ink);
  }
  .divider {
    width: 100%;
    height: 24px;
    margin: 28px 0 10px;
  }
  .divider.lower { margin: 6px 0 28px; }
  .product-name {
    font-size: 150px;
    font-weight: 500;
    font-stretch: 82%;
    line-height: 1;
    letter-spacing: 1px;
    margin: 0;
  }
  .product-type {
    font-size: 54px;
    font-weight: 600;
    font-stretch: 90%;
    line-height: 1.2;
    margin: 0;
  }
  .age {
    margin-top: 30px;
    font-size: 44px;
    font-weight: 600;
    font-stretch: 90%;
    display: flex;
    align-items: baseline;
    gap: 16px;
  }
  .age .age-number {
    font-size: 110px;
    font-weight: 600;
    line-height: 1;
  }
  .specs {
    margin-top: 24px;
    font-size: 22px;
    font-weight: 600;
    letter-spacing: 0.5px;
  }
</style>
</head>
<body>
<main class="canvas">
  <section class="label">
    <div class="brand">
      <div class="brand-dot"></div>
      <div class="brand-name">
        <span class="line-main">Harrowgate</span>
        <span class="line-sub">DISTILLERY</span>
      </div>
    </div>

    <svg class="divider" viewBox="0 0 780 24" aria-hidden="true">
      <line x1="0" y1="12" x2="370" y2="12" stroke="#fefcee" stroke-width="2"/>
      <rect x="382" y="4" width="16" height="16" transform="rotate(45 390 12)" fill="#fefcee"/>
      <line x1="410" y1="12" x2="780" y2="12" stroke="#fefcee" stroke-width="2"/>
    </svg>

    <h1 class="product-name">CEDAR LORNE</h1>

    <svg class="divider lower" viewBox="0 0 780 24" aria-hidden="true">
      <line x1="0" y1="12" x2="370" y2="12" stroke="#fefcee" stroke-width="2"/>
      <rect x="382" y="4" width="16" height="16" transform="rotate(45 390 12)" fill="#fefcee"/>
      <line x1="410" y1="12" x2="780" y2="12" stroke="#fefcee" stroke-width="2"/>
    </svg>

    <p class="product-type">STRAIGHT BOURBON<br>WHISKEY</p>

    <div class="age">
      <span>AGED</span>
      <span class="age-number">3</span>
      <span>YEARS</span>
    </div>

    <p class="specs">750 ML | 84 PROOF | 42% ALC/VOL</p>
  </section>
</main>
</body>
</html>
```